Redesign Powerpoint presentation

Attached is a presentation which needs to be redesigned and made to look more cool and slick.
Reason: Am extending the deadline as I have not recived enough designs that meet my expectations .
Target Market(s)
Marketing heads and managers .All people intersted in sales promotions
Look and feel
Each slider illustrates characteristics of the customer's brand and the style your logo design should communicate.

```html
<!DOCTYPE html>
<html lang="en">
<head>
<meta charset="utf-8">
<title>1. Sale</title>
<link rel="stylesheet" href="https://fonts.googleapis.com/css2?family=Signika:wght@500;600;700&display=swap">
<style>
  :root {
    --green-dark: #023a17;
    --green-mid: #05572a;
    --green-light: #0d6c3c;
    --ink: #111111;
    --brand-ink: #16382f;
    --bg-light: #fafafa;
    --bg-edge: #d6d6d6;
    --white: #ffffff;
  }
  html, body {
    margin: 0;
    padding: 0;
    width: 1200px;
    height: 844px;
    overflow: hidden;
  }
  .slide {
    position: relative;
    width: 1200px;
    height: 844px;
    overflow: hidden;
    background: radial-gradient(ellipse at 62% 45%, var(--bg-light) 0%, #ececec 45%, var(--bg-edge) 100%);
    font-family: "Signika", sans-serif;
  }
  .arrow-shape {
    position: absolute;
    left: 0;
    top: 0;
  }
  .slide-title {
    position: absolute;
    left: 342px;
    top: 90px;
    margin: 0;
    font-size: 93px;
    font-weight: 600;
    line-height: 1;
    color: var(--white);
    letter-spacing: 1px;
  }
  .brand {
    position: absolute;
    left: 898px;
    top: 68px;
    width: 290px;
  }
  .brand-mark {
    position: absolute;
    left: 0;
    top: 20px;
    width: 26px;
    height: 26px;
    border-radius: 50%;
    background: var(--brand-ink);
  }
  .brand-name {
    margin: 0 0 0 38px;
    font-size: 54px;
    font-weight: 600;
    line-height: 0.88;
    color: var(--brand_ink, var(--brand-ink));
  }
  .brand-tagline {
    margin: 10px 0 0 42px;
    font-size: 11.5px;
    font-weight: 600;
    letter-spacing: 0.3px;
    color: var(--brand-ink);
    white-space: nowrap;
  }
  .slide-body {
    position: absolute;
    left: 328px;
    top: 344px;
    width: 820px;
    margin: 0;
    font-size: 31px;
    font-weight: 500;
    line-height: 39px;
    letter-spacing: 0.8px;
    color: var(--ink);
    white-space: nowrap;
  }
</style>
</head>
<body>
<main class="slide">
  <svg class="arrow-shape" width="1200" height="844" viewBox="0 0 1200 844" aria-hidden="true">
    <defs>
      <linearGradient id="arrowFill" x1="0" y1="0" x2="1" y2="0">
        <stop offset="0" stop-color="#023a17"/>
        <stop offset="0.55" stop-color="#05572a"/>
        <stop offset="1" stop-color="#0d6c3c"/>
      </linearGradient>
    </defs>
    <path fill="url(#arrowFill)"
          d="M0 0 H549 L691 146 L561 281 L562 218 C330 222 110 380 66 560 C52 660 100 770 157 844 H0 Z"/>
  </svg>

  <h1 class="slide-title">1.SALE</h1>

  <div class="brand">
    <span class="brand-mark"></span>
    <p class="brand-name">BONUS<br>HARBOR</p>
    <p class="brand-tagline">Trusted Loyalty &amp; Incentive Partners</p>
  </div>

  <p class="slide-body">Before learning more about how to do successful sales<br>and selling, it's important first to get a sense of what<br>sales is, so you can more accurately understand the<br>guidelines, tips and tools provided throughout this<br>topic.<br>There is a general, overall process that successful sales<br>people follow, although there are different perspecti-<br>ves on that process, including names for the various<br>steps along the way.</p>
</main>
</body>
</html>
```